Pick-n-Plate Gift Coupon

About Us-
Pick-n-Plate is a Tasmanian owned food delivery business which delivers meals from an increasing range of selected restaurants. We provide customers with quality food from reputed restaurants at reasonable delivery charges that meet the highest standards of quality and freshness.
We need some gift coupons/vouchers for our privileged customers. We need three designs which are as follows:
1) 10% OFF
2) FREE DELIVERY
3) FREE DELIVERY when you add any Wine/Beer
Coupons should have following:
Pick-n-Plate Logo
Coupon Code: __________
Note:Redeem this coupon on www.picknplate.com.au

```html
<!DOCTYPE html>
<html lang="en">
<head>
<meta charset="utf-8">
<title>Pick-n-Plate Gift Coupons</title>
<link href="https://fonts.googleapis.com/css2?family=PT+Sans:wght@400;700&display=swap" rel="stylesheet">
<style>
  :root {
    --orange: #f07a21;
    --brown: #4a2f22;
    --text: #3a2a22;
    --border: #9a9a9a;
    --paper: #ffffff;
    --crust-light: #f2c27a;
    --crust-deep: #c9752f;
    --sauce: #b8321f;
    --plate: #d9b38c;
  }
  * { margin: 0; padding: 0; box-sizing: border-box; }
  html, body { width: 927px; height: 1200px; overflow: hidden; background: var(--paper); }
  body { position: relative; font-family: "PT Sans", sans-serif; color: var(--text); }

  .coupon {
    position: absolute;
    left: 151px;
    width: 619px;
    height: 279px;
    border: 1px solid var(--border);
    background: var(--paper);
    overflow: hidden;
  }
  .coupon--discount { top: 141px; }
  .coupon--delivery { top: 467px; }
  .coupon--drinks { top: 793px; }

  .food-strip {
    position: absolute;
    top: 0;
    width: 71px;
    height: 100%;
  }
  .food-strip--left {
    left: 0;
    background: linear-gradient(180deg, var(--sauce) 0%, #d9542c 18%, var(--crust-light) 40%, #8a4a2a 55%, var(--crust-deep) 72%, var(--crust-light) 100%);
  }
  .food-strip--right {
    right: 0;
    background: linear-gradient(180deg, #c44a26 0%, var(--crust-light) 28%, #e8a25a 48%, var(--plate) 62%, #b98a5e 82%, #8a5a3a 100%);
  }

  .brand {
    position: absolute;
    top: 19px;
    left: 0;
    right: 0;
    display: flex;
    justify-content: center;
    align-items: center;
    gap: 12px;
  }
  .brand__mark {
    width: 62px;
    height: 62px;
    border-radius: 12px;
    background: var(--brown);
  }
  .brand__name {
    font-size: 32px;
    font-weight: 700;
    color: var(--brown);
    letter-spacing: -0.3px;
  }

  .offer {
    position: absolute;
    left: 0;
    right: 0;
    text-align: center;
    color: var(--orange);
    font-weight: 700;
    line-height: 1;
    letter-spacing: -1px;
  }
  .coupon--discount .offer { top: 110px; font-size: 66px; }
  .coupon--delivery .offer { top: 120px; font-size: 54px; }
  .coupon--drinks .offer { top: 105px; font-size: 54px; }

  .offer__condition {
    position: absolute;
    top: 163px;
    left: 0;
    right: 0;
    text-align: center;
    color: var(--orange);
    font-size: 24px;
    font-weight: 400;
  }

  .details {
    position: absolute;
    top: 210px;
    left: 0;
    right: 0;
    text-align: center;
    font-size: 18px;
    line-height: 27px;
    color: var(--text);
  }
  .details__code-blank {
    display: inline-block;
    width: 94px;
    border-bottom: 1px solid var(--text);
    vertical-align: 3px;
  }
  .details__site { color: var(--orange); font-weight: 700; }
</style>
</head>
<body>

  <section class="coupon coupon--discount">
    <div class="food-strip food-strip--left" role="img" aria-label="Close-up photo of a pizza with olives and peppers"></div>
    <div class="food-strip food-strip--right" role="img" aria-label="Close-up photo of a pizza slice on a wooden board"></div>
    <div class="brand"><span class="brand__mark"></span><span class="brand__name">Pick-n-Plate</span></div>
    <h2 class="offer">10% OFF</h2>
    <p class="details">Coupon Code: <span class="details__code-blank"></span><br>
      Redeem this coupon on <span class="details__site">www.picknplate.com.au</span></p>
  </section>

  <section class="coupon coupon--delivery">
    <div class="food-strip food-strip--left" role="img" aria-label="Close-up photo of a pizza with olives and peppers"></div>
    <div class="food-strip food-strip--right" role="img" aria-label="Close-up photo of a pizza slice on a wooden board"></div>
    <div class="brand"><span class="brand__mark"></span><span class="brand__name">Pick-n-Plate</span></div>
    <h2 class="offer">FREE DELIVERY</h2>
    <p class="details">Coupon Code: <span class="details__code-blank"></span><br>
      Redeem this coupon on <span class="details__site">www.picknplate.com.au</span></p>
  </section>

  <section class="coupon coupon--drinks">
    <div class="food-strip food-strip--left" role="img" aria-label="Close-up photo of a pizza with olives and peppers"></div>
    <div class="food-strip food-strip--right" role="img" aria-label="Close-up photo of a pizza slice on a wooden board"></div>
    <div class="brand"><span class="brand__mark"></span><span class="brand__name">Pick-n-Plate</span></div>
    <h2 class="offer">FREE DELIVERY</h2>
    <p class="offer__condition">when you add any Wine/Beer</p>
    <p class="details">Coupon Code: <span class="details__code-blank"></span><br>
      Redeem this coupon on <span class="details__site">www.picknplate.com.au</span></p>
  </section>

</body>
</html>
```